Comprehensive Wealth Management

We provide the following services:
Asset Protection
Trust Administration
Estate Planning - Wills & Trusts
Management of Assets, Stocks, Bonds, ETF's, and Mutual Funds
Tax Planning
Financial Planning
Multi-Generational Planning
Business Planning
Retirement Planning
Risk Management
Hi Designers, please see the attached link for a sample of our website that you can see what we do and you may or may not use the same colors and style. Be creative please.
http://peterholloway.sitevale-example.com/

Target Market(s)

Widows, Trust beneficiaries, Trustees, retirees and those getting ready for retirement

Contact Information for Business Card

Law Offices of Peter M. Holloway
48217 Corliss Avenue, Suite 206
Woodland Hills, California 91379
p: 818.555.4216
f: 818.555.4290
e: pholloway@fernwickadv.com

Peter M. Holloway, Esq., CPA, CFP

Colors
0293ce
33a6d7
86cae7
0555a3
3377b5
85acd3
00a990
34b8a4
87d0c7

Requirements
Must have
• I would like a design that really pops. I have a sample brochure that has a molecular structure with the various topics on each molecule. I like the various shades of blue. I can send you the brochure sample if you like.
Nice to have
• Very high end design/logo of some kind that has a modern art look. We primarily work with high net worth and ultra high net worth clients. It should be unique looking. Maybe with pretty greens and blues.

```html
<!DOCTYPE html>
<html lang="en">
<head>
<meta charset="utf-8">
<title>Holloway Business Cards</title>
<link rel="stylesheet" href="https://fonts.googleapis.com/css2?family=Pathway+Gothic+One&display=swap">
<style>
  :root {
    --page-bg: #f1f1f1;
    --card-mint: #86d0c7;
    --card-band: #2f8bc0;
    --ink-blue: #2e8ac0;
    --band-text: #a6e2dc;
    --font-main: "Pathway Gothic One", "Arial Narrow", sans-serif;
  }
  * { margin: 0; padding: 0; box-sizing: border-box; }
  html, body {
    width: 1039px; height: 1200px; overflow: hidden;
    background: var(--page-bg);
    font-family: var(--font-main);
  }
  .sheet {
    width: 1039px; height: 1200px;
    display: flex; flex-direction: column; align-items: center;
    justify-content: center; gap: 64px;
  }
  .card {
    position: relative;
    width: 880px; height: 503px;
    background: var(--card-mint);
    text-transform: uppercase;
    overflow: hidden;
  }
  .card-band {
    position: absolute; left: 0; right: 0; bottom: 0;
    background: var(--card-band);
    color: var(--band-text);
  }
  .brand-mark {
    position: absolute; left: 0; right: 0; top: 48px;
    display: flex; align-items: center; justify-content: center; gap: 14px;
    color: var(--ink-blue);
    font-size: 56px; letter-spacing: 4px; line-height: 1;
  }
  .brand-dot {
    width: 22px; height: 22px; border-radius: 50%;
    background: var(--ink-blue);
  }
  /* Front */
  .firm-title {
    position: absolute; left: 0; right: 0; top: 178px;
    text-align: center; color: var(--ink-blue); line-height: 1;
  }
  .firm-kicker { font-size: 27px; letter-spacing: 0.5px; }
  .firm-name { font-size: 42px; letter-spacing: 2px; margin-top: 2px; }
  .card-front .card-band { top: 290px; }
  .contact-left, .contact-right {
    position: absolute; top: 26px;
    font-size: 30px; line-height: 43px;
  }
  .contact-left { left: 36px; }
  .contact-left .credentials { font-size: 22px; }
  .contact-right { right: 36px; text-align: right; }
  .contact-right .label { font-size: 22px; }
  .website {
    position: absolute; left: 0; right: 0; bottom: 20px;
    text-align: center; font-size: 22px; letter-spacing: 0.5px;
  }
  /* Back */
  .tagline {
    position: absolute; left: 0; right: 0; top: 200px;
    text-align: center; color: var(--ink-blue);
    font-size: 34px; letter-spacing: 1.5px;
  }
  .card-back .card-band { top: 300px; }
  .service-list {
    position: absolute; top: 26px; list-style: none;
    font-size: 25px; line-height: 32px;
  }
  .service-list.left { left: 36px; }
  .service-list.right { right: 36px; text-align: right; }
</style>
</head>
<body>
<main class="sheet">
  <section class="card card-front" aria-label="Business card front">
    <div class="brand-mark"><span class="brand-dot"></span><span>Holloway</span></div>
    <div class="firm-title">
      <div class="firm-kicker">The Law Offices of</div>
      <div class="firm-name">Peter M. Holloway</div>
    </div>
    <div class="card-band">
      <div class="contact-left">
        <div>Peter M. Holloway, <span class="credentials">Esq., CPA, CFP</span></div>
        <div>48217 Corliss Ave. Suite 206</div>
        <div>Woodland Hills, CA. 91379</div>
      </div>
      <div class="contact-right">
        <div><span class="label">Phone:</span> 818.555.4216</div>
        <div><span class="label">Fax:</span> 818.555.4290</div>
        <div><span class="label">Email:</span> pholloway@fernwickadv.com</div>
      </div>
      <div class="website">peterholloway.sitevale-example.com</div>
    </div>
  </section>

  <section class="card card-back" aria-label="Business card back">
    <div class="brand-mark"><span class="brand-dot"></span><span>Holloway</span></div>
    <div class="tagline">Comprehensive Wealth Management</div>
    <div class="card-band">
      <ul class="service-list left">
        <li>Asset Protection</li>
        <li>Trust Administration</li>
        <li>Estate Planning - Wills &amp; Trusts</li>
        <li>Management of Assets, Stocks, Bonds, ETF's, and Mutual Funds</li>
        <li>Tax Planning</li>
      </ul>
      <ul class="service-list right">
        <li>Financial Planning</li>
        <li>Multi-Generational Planning</li>
        <li>Business Planning</li>
        <li>Retirement Planning</li>
        <li>Risk Management</li>
      </ul>
    </div>
  </section>
</main>
</body>
</html>
```